Business Card Design Project

1. Show the company logo.
2. Only company email ID and website address to be shown (office@zolotoyveter.fm , www.zolotoyveter.fm).
3. Logo to be provided by us, 2 designs just in case. The logo is made with ' Zolotoy Veter' text, need to be edited so that it shows 'Tikhaya Gavan' instead .
4. Single sided business card, portrait or landscape is not a problem; back side to be filled with colors or a design that matches the logo the best.
5. Logo is to be embossed.
6. We're looking at an English and Russian version.
7. any other better idea is always welcomed.

```html
<!DOCTYPE html>
<html lang="en">
<head>
<meta charset="utf-8">
<title>NeuroVolna – Business Card</title>
<link rel="stylesheet" href="https://fonts.googleapis.com/css2?family=Montserrat:wght@700&family=Arimo:wght@700&display=swap">
<style>
  :root {
    --stage-light: #a6aaac;
    --stage-mid: #5d6163;
    --stage-dark: #1b1e20;
    --card-black: #070a0b;
    --card-mist: #b5c4c3;
    --brand-blue: #1666f5;
    --ink-white: #ffffff;
    --ink-dark: #0d0f10;
    --emboss-text: #bccac9;
    --emboss-blue: #abbfcc;
  }
  * { margin: 0; padding: 0; box-sizing: border-box; }
  html, body { width: 1200px; height: 1183px; overflow: hidden; }
  body {
    position: relative;
    background: linear-gradient(225deg, var(--stage-dark) 0%, var(--stage-mid) 50%, var(--stage-light) 100%);
  }
  .card {
    position: absolute;
    left: 275px;
    width: 667px;
    height: 381px;
    border-radius: 14px;
    overflow: hidden;
  }
  .card--front { top: 187px; background: var(--card-mist); }
  .card--back { top: 602px; background: var(--card-mist); }
  .front-panel {
    position: absolute;
    left: 0; top: 0;
    width: 100%;
    height: 328px;
    background: var(--card-black);
  }
  .wordmark {
    position: absolute;
    left: 0; right: 0;
    top: 0;
    height: 100%;
    display: flex;
    align-items: center;
    justify-content: center;
    gap: 18px;
  }
  .wordmark__dot {
    width: 34px; height: 34px;
    border-radius: 50%;
    background: var(--brand-blue);
    flex: none;
  }
  .wordmark__name {
    font-family: "Montserrat", sans-serif;
    font-weight: 700;
    font-size: 70px;
    letter-spacing: -1px;
    color: var(--ink-white);
    line-height: 1;
  }
  .card--back .wordmark__dot { background: var(--emboss-blue); }
  .card--back .wordmark__name { color: var(--emboss-text); }
  .contact-band {
    position: absolute;
    left: 0; bottom: 0;
    width: 100%;
    height: 53px;
    display: flex;
    align-items: center;
    justify-content: space-between;
    padding: 0 51px 0 48px;
    font-family: "Arimo", sans-serif;
    font-weight: 700;
    font-size: 19px;
    color: var(--ink-dark);
  }
</style>
</head>
<body>
  <section class="card card--front" aria-label="Business card front">
    <div class="front-panel">
      <div class="wordmark">
        <span class="wordmark__dot"></span>
        <span class="wordmark__name">NeuroVolna</span>
      </div>
    </div>
    <div class="contact-band">
      <span class="contact-email">office@zolotoyveter.fm</span>
      <span class="contact-web">www.zolotoyveter.fm</span>
    </div>
  </section>

  <section class="card card--back" aria-label="Business card back with embossed name">
    <div class="wordmark">
      <span class="wordmark__dot"></span>
      <span class="wordmark__name">NeuroVolna</span>
    </div>
  </section>
</body>
</html>
```